Cousin Pellos catering food truck

Need a flyer for a very famous food truck in NYC. We are an established entity since 1971, our specilaty is Greek Food. Please visit our website for more information. We would like a flyer to hand to our existing and new customers, for catering. Whether the truck is on site or for corporate events or weddings. to be more detailed parties weddings corporate events
Cousinpellos.net
twitter/instagram @cousinpellos
Facebook
foursquare
Updates
Please keep in mind , I would like a flyer to focus on our catering. Catering for any occasion. Weddings party's etc...
correct spelling is CATERING
we cater to corporate events, weddings, sweet sixteens, truck can be on site, or we can have food delivered to you
Target Market(s)
looking to book weekend events such as weddings
Industry/Entity Type
Catering
Look and feel
Each slider illustrates characteristics of the customer's brand and the style your logo design should communicate.

```html
<!DOCTYPE html>
<html lang="en">
<head>
<meta charset="utf-8">
<title>Cousin Pellos Catering Flyer</title>
<link rel="stylesheet" href="https://fonts.googleapis.com/css2?family=Oswald:wght@400;500;700&family=Open+Sans:wght@400;600;700&display=swap">
<style>
:root{
  --blue:#1f8fd6;
  --blue-deep:#1467a8;
  --orange:#f26a1b;
  --orange-light:#ff8a2a;
  --ink:#2b2b2b;
  --white:#ffffff;
  --bar:#2d2f33;
}
*{margin:0;padding:0;box-sizing:border-box}
html,body{width:874px;height:1200px;overflow:hidden;background:#e9e9e9}
.flyer{position:relative;width:874px;height:1200px;background:var(--white);overflow:hidden;font-family:"Open Sans",Arial,sans-serif;color:var(--ink)}
.brand{position:absolute;left:40px;top:48px;display:flex;align-items:center;gap:14px}
.brand-mark{width:56px;height:56px;background:var(--blue)}
.brand-name{font-family:"Oswald",Arial,sans-serif;font-weight:700;font-size:40px;color:var(--blue);line-height:1;text-transform:uppercase}
.headline{position:absolute;right:44px;top:22px;text-align:right;font-family:"Oswald",Arial,sans-serif;line-height:1}
.headline .kicker{font-size:42px;font-weight:700;color:var(--orange);letter-spacing:1px}
.headline .main{font-size:92px;font-weight:500;color:var(--ink);letter-spacing:2px}
.stripes{position:absolute;left:0;top:160px;width:874px;height:140px}
.food-photo{position:absolute;left:0;top:235px;width:874px;height:380px;background:radial-gradient(ellipse at 40% 55%,#c9503a 0%,#7a3a2a 30%,#3d4a2a 60%,#2a2a22 100%)}
.blue-panel{position:absolute;left:0;top:560px;width:874px;height:520px}
.intro{position:absolute;left:40px;top:628px;width:590px;color:var(--white)}
.intro .fresh{font-family:"Oswald",Arial,sans-serif;font-weight:700;font-size:44px;color:var(--orange-light);line-height:1}
.intro .greek{font-family:"Oswald",Arial,sans-serif;font-weight:700;font-size:122px;line-height:.95;letter-spacing:2px}
.offer{display:inline-block;margin-top:4px;padding:3px 16px;background:var(--orange);font-family:"Oswald",Arial,sans-serif;font-weight:500;font-size:26px;line-height:1.4;text-transform:uppercase}
.occasions{list-style:none;margin-top:8px;font-size:21px;font-weight:600;line-height:1.35}
.occasions li::before{content:"• "}
.note{margin-top:8px;font-size:14px;line-height:1.4;color:#e5f2fb}
.signup{position:absolute;left:640px;top:630px;width:200px;height:230px}
.signup-text{position:absolute;left:640px;top:650px;width:200px;text-align:center;color:var(--white);text-transform:uppercase}
.signup-text .big{font-family:"Oswald",Arial,sans-serif;font-weight:700;font-size:54px;line-height:1}
.signup-text .small{font-size:16px;font-weight:600;line-height:1.4;margin-top:6px}
.crowd-photo{position:absolute;left:640px;top:860px;width:234px;height:150px;background:linear-gradient(160deg,#9cc4e0,#4c6a80 55%,#2c3a44)}
.menu-line{position:absolute;left:40px;top:1014px;width:590px;font-family:"Oswald",Arial,sans-serif;font-weight:500;font-size:26px;line-height:1.1;color:var(--orange-light);text-transform:uppercase}
.follow{position:absolute;left:40px;top:1092px;display:flex;align-items:center;gap:12px;font-family:"Oswald",Arial,sans-serif;font-size:32px}
.follow .icon{width:30px;height:30px;background:var(--blue)}
.follow .handle{font-weight:500}
.truck-art{position:absolute;left:680px;top:1070px;width:170px;height:76px;background:linear-gradient(180deg,#2a7fc4,#1a5c94);border-radius:8px}
.footer-bar{position:absolute;left:0;top:1150px;width:874px;height:50px;background:var(--bar);display:flex;align-items:center;justify-content:space-between;padding:0 40px;font-family:"Oswald",Arial,sans-serif;color:var(--white)}
.footer-bar .visit{font-size:28px;color:var(--orange-light)}
.footer-bar .visit b{color:var(--white);font-weight:500}
.footer-bar .order{text-align:right;font-size:15px;line-height:1.05;color:var(--orange-light)}
.footer-bar .order span{display:block;font-size:22px;color:var(--white)}
</style>
</head>
<body>
<div class="flyer">
  <div class="brand"><div class="brand-mark"></div><div class="brand-name">Cousin Pellos</div></div>
  <div class="headline"><div class="kicker">TRADITIONAL GREEK</div><div class="main">CUISINE</div></div>

  <div class="food-photo" role="img" aria-label="Platter of grilled Greek meats, vegetables and tomatoes"></div>

  <svg class="stripes" viewBox="0 0 874 140" aria-hidden="true">
    <polygon points="0,30 874,70 874,80 0,40" fill="var(--orange)"/>
    <polygon points="0,45 874,85 874,140 0,75" fill="var(--white)"/>
    <polygon points="0,48 874,88 874,100 0,60" fill="var(--blue)"/>
  </svg>

  <svg class="blue-panel" viewBox="0 0 874 520" aria-hidden="true">
    <polygon points="0,40 874,20 874,520 0,520" fill="var(--blue)"/>
    <polygon points="0,40 874,20 874,32 0,52" fill="var(--blue-deep)"/>
  </svg>

  <div class="intro">
    <div class="fresh">FRESH &amp; AUTHENTIC</div>
    <div class="greek">GREEK</div>
    <div class="offer">We offer catering for</div>
    <ul class="occasions">
      <li>Weddings</li>
      <li>Corporate Events Celebrations</li>
      <li>Birthdays and Anniversaries</li>
    </ul>
    <p class="note">Make sure to specify the number of people you will have attending your event. Let us know about a guest's food accommodations or allergies when placing your order.</p>
  </div>

  <svg class="signup" viewBox="0 0 200 230" aria-hidden="true">
    <polygon points="0,0 200,0 200,180 100,230 0,180" fill="var(--orange)"/>
  </svg>
  <div class="signup-text">
    <div class="big">SIGN UP</div>
    <div class="small">to our newsletter<br>to receive our<br>specials of the day</div>
  </div>

  <div class="crowd-photo" role="img" aria-label="Customers gathered at the food truck"></div>

  <div class="menu-line">We will work with you on a catering<br>menu to include your favorite Greek cuisine</div>

  <div class="follow">
    <span>follow us</span>
    <span class="icon"></span><span class="icon"></span><span class="icon"></span>
    <span class="handle">@cousinpellos</span>
  </div>

  <div class="truck-art" role="img" aria-label="Illustration of the blue food truck"></div>

  <div class="footer-bar">
    <div class="visit">visit us <b>Cousinpellos.net</b></div>
    <div class="order">Order for pick up or delivery<span>From our website</span></div>
  </div>
</div>
</body>
</html>
```